Startup photography business has a new logo, now we need business cards

Design a business card for the two partners of our business.
Our business Brisk Pelican has a new logo and we need to design a business card to showcase it and us.
Our colours of blue and orange are punchy and vivid, but how can we make the most of it on our card?

It should have our name Brisk Pelican
name of partner
phone number
email
website

Industry/Entity Type

Professional Photography

Contact Information for Business Card

Tom Ashworth
+61 400 55 61 72
tom@briskpelican.com.au
briskpelican.com.au

second card
Neil Porter
+61 400 918 263
neil@briskpelican.com.au
briskpelican.com.au

Colors
f37122
f68d4c
33a6d7
0592cd

Requirements
Must have
• one version of our logo, we have included options
• Name
• phone number
• email
• website
Nice to have
• instagram briskpelicanmedia
• twitter briskpelicanmedia
• facebook briskpelicanmedia

```html
<!DOCTYPE html>
<html lang="en">
<head>
<meta charset="utf-8">
<title>Brisk Pelican – Business Card</title>
<link rel="stylesheet" href="https://fonts.googleapis.com/css2?family=Tinos:wght@400;700&display=swap">
<style>
  :root {
    --page-bg: #e4e4e6;
    --card-black: #0c0c0c;
    --card-black-soft: #2a2a2a;
    --orange: #f37122;
    --orange-light: #f68d4c;
    --orange-deep: #e9621a;
    --blue: #33a6d7;
    --blue-deep: #0592cd;
    --white: #ffffff;
  }
  * { box-sizing: border-box; margin: 0; padding: 0; }
  html, body {
    width: 1200px;
    height: 800px;
    overflow: hidden;
    background: var(--page-bg);
    font-family: "Tinos", "Times New Roman", serif;
  }
  .canvas {
    position: relative;
    width: 1200px;
    height: 800px;
  }
  .card {
    position: absolute;
    width: 540px;
    height: 309px;
    border-radius: 6px;
    overflow: hidden;
    box-shadow: 0 10px 24px rgba(0,0,0,0.18);
  }

  /* Front */
  .card-front {
    left: 50px;
    top: 110px;
    background: linear-gradient(160deg, var(--card-black-soft) 0%, var(--card-black) 55%);
  }
  .edge-tab {
    position: absolute;
    width: 20px;
    height: 84px;
    background: var(--orange);
    border-radius: 8px;
  }
  .edge-tab-left { left: -8px; top: 168px; }
  .edge-tab-right { right: -8px; top: 62px; }
  .brand-lockup {
    position: absolute;
    left: 0; right: 0;
    top: 92px;
    display: flex;
    flex-direction: column;
    align-items: center;
    gap: 14px;
  }
  .brand-row {
    display: flex;
    align-items: center;
    gap: 14px;
  }
  .brand-mark {
    width: 46px;
    height: 46px;
    border-radius: 50%;
    background: var(--blue);
  }
  .brand-name {
    font-size: 50px;
    font-weight: 700;
    color: var(--blue);
    letter-spacing: 1px;
  }
  .brand-rule {
    width: 320px;
    height: 2px;
    background: var(--orange);
  }

  /* Back */
  .card-back {
    left: 610px;
    top: 380px;
    background: linear-gradient(100deg, var(--orange-light) 0%, var(--orange) 55%, var(--orange-deep) 100%);
  }
  .back-glow {
    position: absolute;
    right: -60px;
    top: -60px;
    width: 360px;
    height: 360px;
    border-radius: 50%;
    background: radial-gradient(circle, rgba(246,141,76,0.55) 0%, rgba(246,141,76,0.25) 50%, rgba(243,113,34,0) 72%);
  }
  .back-brand {
    position: absolute;
    left: 28px;
    top: 0;
    bottom: 0;
    width: 230px;
    display: flex;
    align-items: center;
    gap: 10px;
  }
  .back-brand .brand-mark {
    width: 34px;
    height: 34px;
    background: var(--white);
    flex: none;
  }
  .back-brand .brand-name {
    color: var(--white);
    font-size: 32px;
    line-height: 1.05;
  }
  .divider {
    position: absolute;
    left: 278px;
    top: 40px;
    width: 3px;
    height: 230px;
    background: var(--white);
  }
  .contact {
    position: absolute;
    left: 300px;
    top: 60px;
    color: var(--white);
    font-size: 17px;
    line-height: 1.35;
  }
  .contact .person {
    font-size: 22px;
    margin-bottom: 6px;
  }
  .social {
    display: flex;
    align-items: center;
    gap: 8px;
    margin-top: 10px;
  }
  .social-dot {
    width: 22px;
    height: 22px;
    border-radius: 50%;
    background: var(--white);
  }
</style>
</head>
<body>
<main class="canvas">

  <section class="card card-front" aria-label="Business card front">
    <span class="edge-tab edge-tab-left"></span>
    <span class="edge-tab edge-tab-right"></span>
    <div class="brand-lockup">
      <div class="brand-row">
        <span class="brand-mark"></span>
        <span class="brand-name">Brisk Pelican</span>
      </div>
      <span class="brand-rule"></span>
    </div>
  </section>

  <section class="card card-back" aria-label="Business card back">
    <div class="back-glow" role="img" aria-label="Soft orange swirl decoration"></div>
    <div class="back-brand">
      <span class="brand-mark"></span>
      <span class="brand-name">Brisk Pelican</span>
    </div>
    <span class="divider"></span>
    <div class="contact">
      <p class="person">Tom Ashworth</p>
      <p>+61 400 55 61 72</p>
      <p>tom@briskpelican.com.au</p>
      <p>briskpelican.com.au</p>
      <div class="social">
        <span class="social-dot"></span>
        <span>briskpelicanmedia</span>
      </div>
    </div>
  </section>

</main>
</body>
</html>
```